Still Brook Trail - Business Card

May try various combos of colors from primary & secondary palette attached below. Logo and Catch phrase previous built logo attached should go on front, but change to color palette options noted. may try various color options from minimal to zen like quality/vibe.
On Front: Attached Logo & Phrase
On Back:
https://stillbrooktrail.com/
415.283.7904
stillbrooktrail@openlanterndesk.ai

Contact Information for Business Card

Daniel R. Forsyth, MD Founder & CEO https://stillbrooktrail.com/ 415.283.7904 stillbrooktrail@openlanterndesk.ai

```html
<!DOCTYPE html>
<html lang="en">
<head>
<meta charset="utf-8">
<title>Still Brook Trail – Business Card</title>
<link rel="stylesheet" href="https://fonts.googleapis.com/css2?family=Tinos&family=Montserrat:wght@400&display=swap">
<style>
  :root {
    --backdrop: #e8e6e3;
    --card-white: #ffffff;
    --maroon: #7a1c1e;
    --ink-light: #ffffff;
    --tagline-grey: #9a9a9a;
    --serif: "Tinos", "Times New Roman", serif;
    --sans: "Montserrat", Arial, sans-serif;
  }
  * { box-sizing: border-box; margin: 0; padding: 0; }
  html, body { width: 1200px; height: 900px; overflow: hidden; }
  body { background: var(--backdrop); position: relative; }

  .card {
    position: absolute;
    top: 302px;
    width: 513px;
    height: 295px;
    border-radius: 24px;
    box-shadow: 0 6px 14px rgba(0,0,0,0.18);
  }
  .card--front { left: 73px; background: var(--card-white); }
  .card--back  { left: 616px; background: var(--maroon); color: var(--ink-light); }

  .front-mark {
    position: absolute;
    left: 207px; top: 56px;
    width: 98px; height: 98px;
    border: 1.5px solid var(--maroon);
    border-radius: 50%;
  }
  .brand-name {
    position: absolute;
    left: 0; right: 0; top: 190px;
    text-align: center;
    font-family: var(--serif);
    font-weight: 400;
    font-size: 41px;
    line-height: 1;
    color: var(--maroon);
  }
  .tagline {
    position: absolute;
    left: 0; right: 0; top: 238px;
    text-align: center;
    font-family: var(--sans);
    font-weight: 400;
    font-size: 15px;
    color: var(--tagline-grey);
  }

  .back-mark {
    position: absolute;
    left: 50px; top: 101px;
    width: 116px; height: 116px;
    border: 1.5px solid var(--ink-light);
    border-radius: 50%;
    display: flex; align-items: center; justify-content: center;
    text-align: center;
    font-family: var(--serif);
    font-size: 17px;
    line-height: 1.15;
  }
  .divider {
    position: absolute;
    left: 201px; top: 56px;
    width: 1.5px; height: 181px;
    background: var(--ink-light);
  }
  .contact {
    position: absolute;
    left: 232px; top: 110px;
    font-family: var(--serif);
    list-style: none;
  }
  .contact li { line-height: 1; }
  .contact__phone { font-size: 21px; }
  .contact__web { font-size: 21px; margin-top: 5px; }
  .contact__email { font-size: 14.5px; margin-top: 8px; }
</style>
</head>
<body>
  <section class="card card--front">
    <div class="front-mark"></div>
    <h1 class="brand-name">Still Brook Trail</h1>
    <p class="tagline">Nurturing Calm Hearts, Breath &amp; Balance</p>
  </section>

  <section class="card card--back">
    <div class="back-mark">Still<br>Brook<br>Trail</div>
    <div class="divider"></div>
    <ul class="contact">
      <li class="contact__phone">415.283.7904</li>
      <li class="contact__web">stillbrooktrail.com</li>
      <li class="contact__email">stillbrooktrail@openlanterndesk.ai</li>
    </ul>
  </section>
</body>
</html>
```